Website for peer to peer car sharing service

Hi all,

We need a web design for a new environmental friendly peer-to-peer car sharing website.

The website will serve as a marketplace where car owners can list their car and drivers that who do not have access to a car can rent a suitable car. It is important for us to emphasis that this is a community where the main purpose is to use the vehicles on the street in a more efficient way.

Attached are five pictures where we have sketched up the five main pages:

File 1. Info site for a particular car.
File 2. Logo.
File 3. Register a car.
File 4. Sign up.
File 5. Search.
File 6. Front page.

The logo for the company is attached (File 2) and it would be ideal to design the website in relation to the logo. The final design should relate to a secure market place which is environmental friendly.

We would like this webpage to be in the same spirit as www.velnoro.it, www.brundale.com, www.plimtrovesite.com, https://wend.kul.net, https://garbelow.com etc.

We look forward to see your designs.

Best regards,
The Trundo Team.

Hi guys, 

Please take :

1) Could you please design icons for for  'FAQ' and 'Insurance' in the header, locate the icons right to the Trundo logo. We only want two icons ('FAQ' and 'Insurance')  right to the Trundo logo.

2) The height of the header should be the same as the header of faplex.com

3) The price tags for the cars (below the top section) should be similar to the price tags at mostanbee.com.

4) We would like you to start to design the other pages (the sub-pages listed in the project description:
a)Info site for a particular car.
b)Register a car. 
c)Search results (similar to http://www.pevrotank.com/find-car).

Please take a look at the picture attached for the sub-pages:

https://files.quenmolt.example/brief_uploads/000001_3_search_000001_brief000001.jpg

https://files.quenmolt.example/brief_uploads/000002_4_infositeforaparticularcar_000002_brief000002.jpg

http://www.quenmolt.example/file.aspx?fileLocation=storage_url/brief_uploads/000003_5_registeracar_brief000003.jpg

Best regards, 
Trundo team 

Target Market(s)

The target market are people from 20-40 years old who are environmental friendly, also tourists who visit the city and would like to rent a car.

Industry/Entity Type

It Company

Requirements
Must have
• It is required that the designer that will be chosen will hand in layered PSD files of each web page.

```html
<!DOCTYPE html>
<html lang="en">
<head>
<meta charset="utf-8">
<title>Trundo – Buy. Insure. Drive.</title>
<link rel="stylesheet" href="https://fonts.googleapis.com/css2?family=Questrial&family=Arimo:wght@400;700&display=swap">
<style>
:root{
  --hero-dark:#1c2430;
  --hero-mid:#3d4d60;
  --hero-light:#7d8c9c;
  --white:#ffffff;
  --green:#7cc433;
  --green-dark:#5fa51f;
  --ink:#1a1a1a;
  --band:#f1f1f1;
  --card-border:#dcdcdc;
  --link-blue:#2f6db5;
  --muted:#8a8a8a;
  --price-red:#b3141b;
  --player:#1d1d1f;
}
*{margin:0;padding:0;box-sizing:border-box}
html,body{width:901px;height:1200px;overflow:hidden;background:var(--white)}
body{position:relative;font-family:"Arimo",Arial,sans-serif;color:var(--ink)}
.hero{position:absolute;left:0;top:0;width:901px;height:530px;
  background:radial-gradient(ellipse at 70% 40%,var(--hero-light) 0%,var(--hero-mid) 35%,var(--hero-dark) 80%);}
.site-header{position:absolute;left:0;top:0;width:901px;height:76px;background:rgba(10,14,20,.55);border-bottom:1px solid rgba(255,255,255,.25)}
.brand{position:absolute;left:100px;top:14px;display:flex;align-items:center;gap:10px;font-family:"Questrial",sans-serif;font-size:36px;color:var(--white)}
.brand-dot{width:30px;height:30px;border-radius:50%;background:var(--green)}
.main-nav{position:absolute;top:27px;right:0;font-family:"Questrial",sans-serif;font-size:17px;color:var(--white)}
.main-nav span{position:absolute;white-space:nowrap}
.hero-title{position:absolute;left:0;top:165px;width:901px;text-align:center;font-family:"Questrial",sans-serif;font-size:80px;font-weight:700;letter-spacing:-1px;color:var(--white);text-shadow:0 2px 4px rgba(0,0,0,.4)}
.hero-lead{position:absolute;left:240px;top:278px;width:420px;text-align:center;font-family:"Questrial",sans-serif;font-size:18px;line-height:21.5px;color:var(--white)}
.search-input{position:absolute;left:193px;top:383px;width:357px;height:45px;border-radius:6px;background:var(--white);border:2px solid #cfd3d8;box-shadow:inset 0 2px 6px rgba(0,0,0,.25)}
.search-button{position:absolute;left:561px;top:383px;width:147px;height:45px;border-radius:5px;background:linear-gradient(var(--green),var(--green-dark));font-family:"Questrial",sans-serif;font-size:17px;color:#1f2a12;display:flex;align-items:center;justify-content:center}
.listings{position:absolute;left:0;top:530px;width:901px;height:329px;background:var(--band)}
.car-card{position:absolute;top:53px;width:212px;height:222px;background:var(--white);border:1px solid var(--card-border)}
.car-photo{position:absolute;left:15px;top:15px;width:181px;height:114px;border:1px solid #cfcfcf}
.owner-avatar{position:absolute;left:15px;top:141px;width:58px;height:58px;border-radius:50%;border:3px solid #e4e4e4;background:linear-gradient(#8a7a6a,#4a4038)}
.car-info{position:absolute;left:82px;top:146px;font-size:10.5px;line-height:13px}
.owner-name{color:var(--link-blue)}
.car-model{color:var(--ink)}
.car-city{color:var(--muted)}
.car-price{color:#333}
.car-price b{font-weight:400;color:var(--price-red)}
.feature-title{position:absolute;left:135px;top:946px;font-size:29px;font-weight:700;color:var(--green)}
.feature-sub{position:absolute;left:135px;top:998px;font-size:16.5px;font-weight:700;line-height:20px}
.feature-body{position:absolute;left:135px;top:1047px;width:282px;font-size:13.5px;line-height:16.2px}
.video{position:absolute;left:455px;top:956px;width:322px;height:190px;background:linear-gradient(135deg,#3a2a5a 0%,#8a1e22 45%,#d2423a 60%,#2a2030 100%)}
.video-controls{position:absolute;left:0;bottom:0;width:322px;height:22px;background:var(--player);font-size:7px;color:#ccc}
.video-controls span{position:absolute;top:7px}
</style>
</head>
<body>
<section class="hero">
  <div role="img" aria-label="Blurred row of parked cars" style="position:absolute;inset:0"></div>
  <header class="site-header">
    <div class="brand"><span class="brand-dot"></span>Trundo</div>
    <nav class="main-nav">
      <span style="left:-355px">List your Car</span>
      <span style="left:-236px">Login</span>
      <span style="left:-166px">Sign up</span>
    </nav>
  </header>
  <h1 class="hero-title">Buy. Insure. Drive.</h1>
  <p class="hero-lead">At trundo we make it easy to find your next car (new or used) along with better car insurance, while giving you the best possible deal.</p>
  <div class="search-input"></div>
  <div class="search-button">Find a Car</div>
</section>

<section class="listings">
  <article class="car-card" style="left:128px">
    <div class="car-photo" role="img" aria-label="Dark grey sedan parked by trees" style="background:linear-gradient(#4f7a3a,#6b8a5a 55%,#9a9a92)"></div>
    <div class="owner-avatar" role="img" aria-label="Owner profile photo"></div>
    <div class="car-info"><div class="owner-name">tomas</div><div class="car-model">Halvern Legato</div><div class="car-city">San Francisco, CA</div><div class="car-price"><b>$ 8.50</b> / hour</div></div>
  </article>
  <article class="car-card" style="left:345px">
    <div class="car-photo" role="img" aria-label="Grey sedan in front of a metal fence" style="background:linear-gradient(#3f6fa8,#8d9aa6 35%,#a8acae 70%,#9a9a98)"></div>
    <div class="owner-avatar" role="img" aria-label="Owner profile photo" style="background:linear-gradient(#9aa04a,#4a4a2a)"></div>
    <div class="car-info"><div class="owner-name">leo marden</div><div class="car-model">Morrow Jessa</div><div class="car-city">San Francisco, CA</div><div class="car-price"><b>$ 7.50</b> / hour</div></div>
  </article>
  <article class="car-card" style="left:562px">
    <div class="car-photo" role="img" aria-label="Light blue small hatchback by a building" style="background:linear-gradient(#c8cacc,#8ab4c4 55%,#7a7a78)"></div>
    <div class="owner-avatar" role="img" aria-label="Owner profile photo" style="background:linear-gradient(#b03a3a,#3a2a2a)"></div>
    <div class="car-info"><div class="owner-name">kiro</div><div class="car-model">Pico Corran</div><div class="car-city">San Francisco, CA</div><div class="car-price"><b>$ 8.50</b> / hour</div></div>
  </article>
</section>

<h2 class="feature-title">Looking for a car.</h2>
<h3 class="feature-sub">Select vehicle and give us<br>your information</h3>
<p class="feature-body">Just tell us the make and model and how to get in touch with you.Just tell us the make and model and how to get in touch with you.Just tell us the make and model and how to get in touch with you.Just tell us the make and model and how to get in touch with you..</p>

<div class="video" role="img" aria-label="Video of a red sports car on a lit city street">
  <div class="video-controls">
    <svg width="322" height="22" style="position:absolute;left:0;top:0">
      <rect x="9" y="7" width="2" height="7" fill="#ddd"/><rect x="13" y="7" width="2" height="7" fill="#ddd"/>
      <line x1="24" y1="0" x2="24" y2="22" stroke="#333"/>
      <rect x="56" y="9" width="140" height="3" fill="#555"/><rect x="56" y="9" width="55" height="3" fill="#888"/><rect x="56" y="9" width="18" height="3" fill="var(--green)"/>
      <line x1="240" y1="0" x2="240" y2="22" stroke="#333"/><line x1="263" y1="0" x2="263" y2="22" stroke="#333"/>
      <path d="M248 7h3M248 7v3M257 7h-3M257 7v3M248 15h3M248 15v-3M257 15h-3M257 15v-3" stroke="#ccc" fill="none"/>
      <rect x="272" y="9" width="2" height="5" fill="#ccc"/>
      <g fill="var(--green)"><rect x="280" y="9" width="2" height="4"/><rect x="284" y="9" width="2" height="4"/><rect x="288" y="9" width="2" height="4"/><rect x="292" y="9" width="2" height="4"/><rect x="296" y="9" width="2" height="4"/><rect x="300" y="9" width="2" height="4"/><rect x="304" y="9" width="2" height="4"/></g>
    </svg>
    <span style="left:33px">00:10</span><span style="left:217px">02:18</span>
  </div>
</div>
</body>
</html>
```